Flyer Design Project

I need an a5 sized flyer designed for my companys Mindfulness Based Stress Reduction course. I would like it to look peaceful but I would like the designer to be a little creative I don't want it to look like every other boring wellness brochure. No cliched images please. The course is about Mindfulness, there is yoga and meditation involved, again don't want your typical yoga and meditation images on it. I want it to look interesting and different.

The attached document has two pages each page should be one side of the leaflet.

Target Market(s)

alternative people who are interested in wellness, stressed out people and people who have health issues and could benefit from Mindfulness

Industry/Entity Type

Wellness

Requirements
Must have
• I want the fact that we are donating to charity to be obvious. But not in a showing off way. I want it known but NOT hey look at how wonderful I am.

Nice to have
• The font similar to my website.

http://www.quietbirchgrovewellness.com
Should not have
• Cheesy cliched images of yoga and meditation.

```html
<!DOCTYPE html>
<html lang="en">
<head>
<meta charset="utf-8">
<title>Mindfulness Based Stress Reduction – Flyer</title>
<link href="https://fonts.googleapis.com/css2?family=Open+Sans:ital,wght@0,600;1,300;1,400&family=PT+Sans:ital,wght@0,700;1,700&display=swap" rel="stylesheet">
<style>
  :root {
    --paper: #ffffff;
    --petal-light: #fdf1ef;
    --petal-mid: #f8d9dc;
    --petal-deep: #f2c0c8;
    --petal-warm: #fbe6cf;
    --title-pink: #ee6a86;
    --leaf-green: #7d9b1f;
    --body-grey: #6a6a6a;
  }
  * { margin: 0; padding: 0; box-sizing: border-box; }
  html, body { width: 1200px; height: 859px; overflow: hidden; background: var(--paper); }
  body { position: relative; font-family: "Open Sans", Arial, sans-serif; color: var(--body-grey); }

  .page {
    position: absolute; top: 22px; width: 575px; height: 816px; overflow: hidden;
  }
  .page--front { left: 22px; }
  .page--back { left: 604px; }

  .page__backdrop { position: absolute; inset: 0; }
  .page--front .page__backdrop {
    background:
      radial-gradient(ellipse at 15% 20%, var(--petal-light) 0%, transparent 55%),
      radial-gradient(ellipse at 80% 75%, var(--petal-warm) 0%, transparent 50%),
      radial-gradient(ellipse at 10% 85%, var(--petal-deep) 0%, transparent 45%),
      linear-gradient(160deg, var(--petal-mid), var(--petal-light) 50%, var(--petal-mid));
  }
  .page--back .page__backdrop {
    background:
      radial-gradient(ellipse at 30% 10%, var(--petal-light) 0%, transparent 50%),
      radial-gradient(ellipse at 85% 30%, var(--petal-warm) 0%, transparent 45%),
      radial-gradient(ellipse at 20% 80%, var(--petal-deep) 0%, transparent 50%),
      linear-gradient(200deg, var(--petal-mid), var(--petal-light) 55%, var(--petal-mid));
  }

  .content { position: absolute; }
  .page--front .content { left: 58px; top: 70px; width: 462px; }
  .page--back .content { left: 59px; top: 88px; width: 450px; }

  .flyer-title {
    font-family: "PT Sans", Arial, sans-serif; font-style: italic; font-weight: 700;
    font-size: 46px; line-height: 44px; color: var(--title-pink); letter-spacing: 0.3px;
  }
  .section-heading {
    font-family: "Open Sans", Arial, sans-serif; font-weight: 600; font-style: italic;
    font-size: 16.5px; color: var(--leaf-green); line-height: 22px;
  }
  .body-copy {
    font-style: italic; font-weight: 300; font-size: 13.6px; line-height: 19px;
  }
  .body-copy + .body-copy { margin-top: 19px; }
  .feature-list {
    list-style: none; font-style: italic; font-weight: 300; font-size: 13.6px; line-height: 19px;
    margin: 19px 0 19px 24px;
  }
  .feature-list li { position: relative; padding-left: 14px; }
  .feature-list li::before { content: "•"; position: absolute; left: 0; font-style: normal; }
  .web-link { font-style: normal; font-weight: 400; }

  .page--front .flyer-title { margin-bottom: 26px; }
  .page--front .section-heading { margin-bottom: 10px; }
  .page--front .section-heading.second { margin-top: 20px; }

  .page--back .section-heading { margin-bottom: 12px; }
  .page--back .feature-list { margin-left: 24px; }

  .brand {
    position: absolute; left: 0; width: 575px; top: 640px; text-align: center;
  }
  .brand__mark {
    display: block; width: 30px; height: 30px; margin: 0 auto 10px; background: var(--leaf-green);
  }
  .brand__name {
    font-family: "Open Sans", Arial, sans-serif; font-weight: 600; font-size: 15px; color: var(--leaf-green);
  }
  .brand__url {
    position: absolute; left: 0; width: 575px; top: 720px; text-align: center;
    font-family: "Open Sans", Arial, sans-serif; font-weight: 600; font-size: 14.5px; color: var(--leaf-green);
  }
</style>
</head>
<body>

<section class="page page--front">
  <div class="page__backdrop" role="img" aria-label="Soft-focus pink and peach flower petals washed across the page"></div>
  <div class="content">
    <h1 class="flyer-title">Mindfulness Based<br>Stress Reduction</h1>

    <h2 class="section-heading">What is Mindfulness?</h2>
    <p class="body-copy">Put simply, mindfulness is about being aware of the present moment, without being caught up in ruminating thoughts or worrying about the past or the future. Mindlessness can result in loss of awareness and in you becoming disconnected from your life. Mindfulness gives us the ability to live more fully as it allows the body and mind to become calmer and more aware.</p>

    <h2 class="section-heading second">What is Mindfulness Based Stress Reduction (MBSR)?</h2>
    <p class="body-copy">MBSR uses mindful mediation and mindful movement as its basis. The practises have shown over two decades to be transforming in the lives of countless course attendees.</p>
    <p class="body-copy">Published reports point out that the majority of course attendees who complete the 8 weeks:</p>
    <ul class="feature-list">
      <li>Are more aware</li>
      <li>Have decreased physical and psychological symptoms</li>
      <li>Are able to relax and manage stress</li>
      <li>Have reduced pain levels or an improved ability to cope<br>with pain levels that may or may not go away</li>
      <li>Live more fully</li>
      <li>Have improved self esteem and reduced anxiety</li>
      <li>Are able to cope better in stressful situations</li>
    </ul>
    <p class="body-copy">Our MBSR courses are closely structured on the approach developed by Dr Alan Merrow and his associates at the Northbrook University Medical Centre.</p>
  </div>
</section>

<section class="page page--back">
  <div class="page__backdrop" role="img" aria-label="Soft-focus pink and peach flower petals washed across the page"></div>
  <div class="content">
    <h2 class="section-heading">Mindfulness Based Stress Reduction Course</h2>
    <p class="body-copy">The Mindfulness Based Stress Reduction course offered by Quiet Birch Grove Wellness provides students with a basis in understanding mindfulness, through mediation and body movement. It allows students a learning environment that is safe and inclusive of all types of people.</p>
    <p class="body-copy" style="margin-top:32px">During the 8 week course, students will have access to the following:</p>
    <ul class="feature-list">
      <li>2 hour weekly sessions and a daylong retreat at week 7.</li>
      <li>Guided instruction in formal and informal mindfulness practise.</li>
      <li>Mindfulness movement exercises.</li>
      <li>Activities in applying mindfulness to everyday living.</li>
      <li>Personal guidance and peer support via a secure online forum.</li>
      <li>Daily assignments.</li>
      <li>A FREE copy of Whole Weather Living by Alan Merrow</li>
      <li>FREE mp3 and instructional movement videos to download</li>
      <li>10% of this course is donated to charity – For this month’s charitable cause, please see our website for details – <span class="web-link">www.quietbirchgrovewellness.com</span></li>
    </ul>
  </div>

  <div class="brand">
    <span class="brand__mark"></span>
    <span class="brand__name">Quiet Birch Grove Wellness</span>
  </div>
  <p class="brand__url">www.quietbirchgrovewellness.com</p>
</section>

</body>
</html>
```